Now Leasing Banner

Looking for a banner that says the following information approx 4' x 30'

Now Leasing Maplewood Terrace 925-318-6054

Target Market(s)

Drive by traffic

Industry/Entity Type

Residential property management

Requirements
Must have
• Clear and readable from a distance

```html
<!DOCTYPE html>
<html lang="en">
<head>
<meta charset="utf-8">
<title>Now Leasing Banner – Maplewood Terrace</title>
<link rel="stylesheet" href="https://fonts.googleapis.com/css2?family=Oswald:wght@600&family=Archivo:wght@800&display=swap">
<style>
  :root {
    --page-bg: #ffffff;
    --forest: #33594a;
    --sage-light: #e7e8e1;
    --sage-mid: #d6dbc4;
    --sage-deep: #bcc69e;
    --sage-edge: #a3ae84;
    --cream: #eef0e4;
    --cream-shade: #b9c2a0;
    --white: #ffffff;
    --frame: #c9ccc2;
  }
  html, body {
    margin: 0;
    padding: 0;
    width: 1200px;
    height: 325px;
    overflow: hidden;
    background: var(--page-bg);
  }
  .banner {
    display: block;
    width: 1200px;
    height: 325px;
  }
  .property-name {
    font-family: "Oswald", "Arial Narrow", sans-serif;
    font-weight: 600;
    fill: var(--forest);
  }
  .leasing-headline,
  .leasing-phone {
    font-family: "Archivo", "Arial Black", Arial, sans-serif;
    font-weight: 800;
  }
  .leasing-phone { fill: var(--white); }
</style>
</head>
<body>
<svg class="banner" viewBox="0 0 1200 325" xmlns="http://www.w3.org/2000/svg" role="img" aria-label="Maplewood Terrace, now leasing, 925.318.6054">
  <defs>
    <linearGradient id="panelFill" x1="0" y1="0" x2="0" y2="1">
      <stop offset="0" stop-color="var(--sage-light)"/>
      <stop offset="0.5" stop-color="var(--sage-mid)"/>
      <stop offset="1" stop-color="var(--sage-deep)"/>
    </linearGradient>
    <linearGradient id="headlineFill" x1="0" y1="0" x2="0" y2="1">
      <stop offset="0" stop-color="var(--cream)"/>
      <stop offset="0.55" stop-color="var(--cream)"/>
      <stop offset="1" stop-color="var(--cream-shade)"/>
    </linearGradient>
    <filter id="softShadow" x="-5%" y="-20%" width="110%" height="140%">
      <feDropShadow dx="0" dy="2" stdDeviation="2" flood-color="#000" flood-opacity="0.25"/>
    </filter>
  </defs>

  <!-- banner body -->
  <g class="banner-body" filter="url(#softShadow)">
    <rect class="banner-base" x="41" y="87" width="1114" height="152" fill="var(--forest)" stroke="var(--frame)" stroke-width="1"/>
  </g>

  <!-- name panel with curved edge -->
  <path class="name-panel-edge" d="M41 87 H590 Q636 115 634 163 Q632 208 590 239 H41 Z" fill="var(--sage-edge)"/>
  <path class="name-panel" d="M41 87 H588 Q624 116 622 163 Q620 207 588 239 H41 Z" fill="url(#panelFill)"/>

  <text class="property-name" x="69" y="206" font-size="118" textLength="508" lengthAdjust="spacingAndGlyphs">MAPLEWOOD TERRACE</text>

  <!-- leasing block -->
  <text class="leasing-headline" x="675" y="154" font-size="66" textLength="448" lengthAdjust="spacingAndGlyphs" fill="url(#headlineFill)" filter="url(#softShadow)">NOW LEASING</text>
  <text class="leasing-phone" x="675" y="220" font-size="68" textLength="445" lengthAdjust="spacingAndGlyphs" filter="url(#softShadow)">925.318.6054</text>
</svg>
</body>
</html>
```